QVAR Individual and Corporate Development Business Card Design

QVAR needs a business card design that is aligned with it's values and targetted markets. Harmonic Lattice of Cognition Network's self diagnosis model and tools, which can be used for personal improvement and team/business performance enhancement, is based on the learnings of over 20 years of medical practitioning. QVAR supercharges personal effectiveness and awareness to also increase team and business performance.

The targetted markets are high performance individuals and teams who aspire seek to enhance their capabilities and achieve their absolute best potential.

Look and feel for the business card design we are looking for is high technology, premium, fresh, new and medical.

Target Market(s)

Industry/Entity Type

Business Consultant

Contact Information for Business Card

Logo, Full Name, Title, Phone number, Email, company name, Address,

Font styles to use
Sans Serif

Requirements
Must have
• Tag line: Maximising Performance for Highly Effective People
• Please use same colours as the logo.

```html
<!DOCTYPE html>
<html lang="en">
<head>
<meta charset="utf-8">
<title>QVAR Business Card</title>
<link rel="stylesheet" href="https://fonts.googleapis.com/css2?family=Michroma&family=Open+Sans:wght@400;600&display=swap">
<style>
  :root {
    --bg: #2a2a2c;
    --card-dark: #070707;
    --card-light: #ffffff;
    --teal: #22b5c9;
    --blue: #2f7fcf;
    --blue-light: #5fa3de;
    --blue-deep: #1f6cc0;
    --silver: #b9bcc1;
    --rule: #7a7f86;
    --white: #ffffff;
  }
  * { margin: 0; padding: 0; box-sizing: border-box; }
  html, body { width: 1200px; height: 900px; overflow: hidden; }
  body {
    background: var(--bg);
    display: flex;
    flex-direction: column;
    align-items: center;
    justify-content: center;
    gap: 40px;
    font-family: "Open Sans", Arial, sans-serif;
  }
  .card {
    width: 700px;
    height: 400px;
    position: relative;
    overflow: hidden;
    box-shadow: 0 10px 30px rgba(0,0,0,.45);
  }
  .card--back { background: var(--card-dark); }
  .card--front { background: var(--card-light); }

  .brand {
    position: absolute;
    display: flex;
    flex-direction: column;
    align-items: flex-start;
    z-index: 1;
  }
  .brand__name {
    font-family: "Michroma", "Open Sans", sans-serif;
    color: var(--teal);
    line-height: 1;
    letter-spacing: 4px;
  }
  .brand__rule {
    height: 2px;
    background: var(--rule);
    width: 100%;
  }
  .brand__full {
    font-family: "Michroma", "Open Sans", sans-serif;
    color: var(--teal);
    text-transform: uppercase;
    line-height: 1.25;
    letter-spacing: 1px;
  }
  .card--back .brand { left: 150px; top: 110px; }
  .card--back .brand__name { font-size: 96px; }
  .card--back .brand__rule { margin: 12px 0 10px; }
  .card--back .brand__full { font-size: 19px; }

  .card--front .brand { left: 110px; top: 58px; }
  .card--front .brand__name { font-size: 54px; letter-spacing: 3px; }
  .card--front .brand__rule { margin: 7px 0 6px; }
  .card--front .brand__full { font-size: 10.5px; letter-spacing: .5px; }

  .wave { position: absolute; inset: 0; width: 100%; height: 100%; }

  .person {
    position: absolute;
    left: 90px;
    bottom: 58px;
    color: var(--white);
  }
  .person__name { font-size: 34px; font-weight: 400; line-height: 1.1; }
  .person__title { font-size: 15px; padding-left: 26px; }

  .contact {
    position: absolute;
    right: 40px;
    top: 160px;
    list-style: none;
    color: var(--white);
    font-size: 16px;
    line-height: 1.6;
  }
  .contact li { display: flex; justify-content: flex-end; align-items: center; gap: 8px; }
  .contact svg { width: 15px; height: 15px; fill: var(--white); flex: none; }
  .contact .contact__cont { padding-right: 23px; }
</style>
</head>
<body>

  <section class="card card--back">
    <div class="brand">
      <span class="brand__name">QVAR</span>
      <span class="brand__rule"></span>
      <span class="brand__full">Harmonic Lattice<br>of Cognition Network</span>
    </div>
  </section>

  <section class="card card--front">
    <svg class="wave" viewBox="0 0 700 400" aria-hidden="true">
      <defs>
        <radialGradient id="blueFill" cx="0.62" cy="0.55" r="0.7">
          <stop offset="0" stop-color="#6aaae0"/>
          <stop offset="1" stop-color="#1f6cc0"/>
        </radialGradient>
      </defs>
      <path d="M0,252 C200,260 360,237 460,142 C540,64 600,22 700,8 L700,400 L0,400 Z" fill="url(#blueFill)"/>
      <path d="M0,240 C200,248 350,226 450,133 C530,58 595,16 680,0" fill="none" stroke="#b9bcc1" stroke-width="8"/>
      <path d="M20,222 C200,228 320,212 425,132 C505,66 570,22 640,0" fill="none" stroke="#2f7fcf" stroke-width="4"/>
    </svg>

    <div class="brand">
      <span class="brand__name">QVAR</span>
      <span class="brand__rule"></span>
      <span class="brand__full">Harmonic Lattice<br>of Cognition Network</span>
    </div>

    <ul class="contact">
      <li>(01) 0000 8888
        <svg viewBox="0 0 24 24"><path d="M6.6 10.8a15 15 0 0 0 6.6 6.6l2.2-2.2a1 1 0 0 1 1-.25 11.4 11.4 0 0 0 3.6.57 1 1 0 0 1 1 1V20a1 1 0 0 1-1 1A17 17 0 0 1 3 4a1 1 0 0 1 1-1h3.5a1 1 0 0 1 1 1c0 1.25.2 2.45.57 3.57a1 1 0 0 1-.25 1z"/></svg>
      </li>
      <li>info@yourdomain.com
        <svg viewBox="0 0 24 24"><path d="M2 5h20v14H2z M3 6.5v.3l9 6 9-6v-.3z" fill-rule="evenodd"/></svg>
      </li>
      <li>Suites 14/15, Level 3
        <svg viewBox="0 0 24 24"><path d="M12 2a7 7 0 0 0-7 7c0 5.2 7 13 7 13s7-7.8 7-13a7 7 0 0 0-7-7zm0 9.5A2.5 2.5 0 1 1 12 6.5a2.5 2.5 0 0 1 0 5z"/></svg>
      </li>
      <li class="contact__cont">48 Harbour Rd Kestrel Bay</li>
    </ul>

    <div class="person">
      <div class="person__name">Your Name</div>
      <div class="person__title">Manager</div>
    </div>
  </section>

</body>
</html>
```